Design for schnapps bottle label "Sol Terrado"

Hi! On a small land lot we are producing our own Italian schnapps "Grappa". For the bottles we would like to modernize our current labes that you find below. The two cats looking at each other should remain, but updated and more modern. I am very much looking forward to your suggestions. Best, Joel

Target Market(s)

Schnapps bottle label

Requirements
Must have
• Cats should resemble the cats that are decorating the house entry (see attached), however, should have a more modern appearance.

Text elements should remain: "Grappa", "Sol Terrado", "Legnoso", "[Vintage Year], "Raccolta No", "Vol %"
Should not have
• Current ornament can be used, replaced or deleted (whatever looks best)

```html
<!DOCTYPE html>
<html lang="it">
<head>
<meta charset="utf-8">
<title>Grappa legnoso 2015 – Sol Terrado</title>
<link rel="stylesheet" href="https://fonts.googleapis.com/css2?family=Berkshire+Swash&family=Sacramento&family=Marcellus&display=swap">
<style>
  :root {
    --backdrop-light: #a29b98;
    --backdrop-dark: #6f6866;
    --paper: #ececeb;
    --paper-shade: #e2e2e1;
    --ink: #1e1e1e;
    --cat-ink: #2a2a2a;
    --olive: #8b8b14;
    --olive-light: #b3b33a;
    --olive-dark: #5e5e0c;
  }
  * { box-sizing: border-box; margin: 0; padding: 0; }
  html, body { width: 1200px; height: 991px; overflow: hidden; }
  body {
    background: radial-gradient(ellipse at 35% 40%, var(--backdrop-light), var(--backdrop-dark));
    position: relative;
  }
  .label {
    position: absolute;
    left: 280px; top: 45px;
    width: 640px; height: 900px;
    background: radial-gradient(ellipse at 50% 40%, var(--paper), var(--paper-shade));
    box-shadow: 0 6px 22px rgba(0,0,0,.25);
    overflow: hidden;
  }
  .ornament {
    position: absolute; left: 27px; top: 10px;
    width: 586px; height: 74px;
    background: linear-gradient(90deg, transparent, rgba(139,139,20,.35) 15%, rgba(139,139,20,.5) 50%, rgba(139,139,20,.35) 85%, transparent);
    border-radius: 40px;
  }
  .title {
    position: absolute; left: 0; right: 0; top: 100px;
    text-align: center;
    font-family: "Berkshire Swash", serif;
    font-weight: 400;
    font-size: 136px; line-height: 150px;
    color: var(--ink);
  }
  .style-line {
    position: absolute; left: 0; right: 0; top: 278px;
    height: 96px;
    text-align: center;
    white-space: nowrap;
    line-height: 96px;
  }
  .style-name {
    font-family: "Sacramento", cursive;
    font-size: 92px; color: var(--ink);
  }
  .vintage {
    font-family: "Marcellus", serif;
    font-size: 44px; color: var(--olive);
    margin-left: 4px;
  }
  .connector {
    position: absolute; left: 0; right: 0; top: 372px;
    height: 52px;
    text-align: center;
    font-family: "Sacramento", cursive;
    font-size: 56px; line-height: 52px;
    color: var(--ink);
    padding-left: 30px;
  }
  .cats {
    position: absolute; left: 84px; top: 432px;
    width: 472px; height: 140px;
    background: radial-gradient(closest-side, var(--cat-ink) 70%, rgba(42,42,42,0) 100%);
  }
  .brand {
    position: absolute; left: 0; right: 0; top: 590px;
    text-align: center;
    font-family: "Berkshire Swash", serif;
    font-weight: 400;
    font-size: 92px; line-height: 110px;
    color: var(--ink);
    white-space: nowrap;
  }
  .brand .cap { color: var(--olive); }
  .batch, .strength {
    position: absolute; top: 756px;
    font-family: "Marcellus", serif;
    font-size: 26px; line-height: 40px;
    color: var(--ink);
    white-space: nowrap;
  }
  .batch { left: 26px; }
  .strength { right: 26px; }
  .batch .script, .strength .script {
    font-family: "Sacramento", cursive; font-size: 38px;
  }
  .band {
    position: absolute; left: 0; right: 0; bottom: 0;
    height: 76px;
    background: linear-gradient(100deg, var(--olive-dark), var(--olive) 30%, var(--olive-light) 55%, var(--olive) 80%, var(--olive-dark));
  }
</style>
</head>
<body>
  <main class="label">
    <div class="ornament" role="img" aria-label="Olive green swirling scroll ornament"></div>
    <h1 class="title">Grappa</h1>
    <p class="style-line"><span class="style-name">“legnoso”</span><span class="vintage">2015</span></p>
    <p class="connector">di</p>
    <div class="cats" role="img" aria-label="Two black cat silhouettes crouching and facing each other, tails curled"></div>
    <p class="brand"><span class="cap">S</span>ol <span class="cap">T</span>errado</p>
    <p class="batch"><span class="script">Raccolta No.</span> 01</p>
    <p class="strength">41.0 <span class="script">Vol</span></p>
    <div class="band" role="img" aria-label="Olive green band with bold geometric pattern"></div>
  </main>
</body>
</html>
```